Crit postcard design

I am in charge of getting a postcard 5x7 designed for 14 artists having a gallery exhibition. We would like to use our
photo(s) with the 14 names on the front. Back of card would have gallery information.
Am sending jpeg of a past card, four images to choose from and the text for back of card.

Artists

```html
<!DOCTYPE html>
<html lang="en">
<head>
<meta charset="utf-8">
<title>Twelve Painters – Exhibition Postcard</title>
<link rel="stylesheet" href="https://fonts.googleapis.com/css2?family=PT+Sans:wght@700&display=swap">
<style>
  :root {
    --page-bg: #d9d9d9;
    --card-white: #ffffff;
    --ink: #1c1c1c;
    --paint-yellow: #e2c62c;
    --paint-orange: #d9812a;
    --paint-dark: #2a2630;
    --column-tint: #ddd07a;
    --column-strip: #ece08e;
    --column-edge: rgba(120, 110, 60, 0.35);
  }
  * { box-sizing: border-box; margin: 0; padding: 0; }
  html, body {
    width: 1200px;
    height: 900px;
    overflow: hidden;
    background: var(--page-bg);
  }
  .postcard {
    position: absolute;
    left: 40px;
    top: 50px;
    width: 1120px;
    height: 800px;
    background: var(--card-white);
    overflow: hidden;
    font-family: "PT Sans", "Helvetica Neue", Arial, sans-serif;
  }
  .postcard__title {
    position: absolute;
    left: 0;
    right: 0;
    top: 64px;
    text-align: center;
    font-weight: 700;
    font-size: 106px;
    line-height: 1;
    font-variant: small-caps;
    letter-spacing: 5px;
    white-space: nowrap;
    color: var(--ink);
    z-index: 1;
  }
  .postcard__artwork {
    position: absolute;
    left: 0;
    top: 152px;
    width: 1120px;
    height: 648px;
    z-index: 2;
    background: linear-gradient(135deg, var(--paint-dark) 0%, var(--paint-yellow) 55%, var(--paint-orange) 100%);
  }
  .artist-column {
    position: absolute;
    left: 0;
    top: 152px;
    width: 318px;
    height: 648px;
    z-index: 3;
    background: var(--column-tint);
    border-right: 1px solid var(--column-edge);
  }
  .artist-column__strip {
    position: absolute;
    left: 50px;
    top: 0;
    width: 214px;
    height: 100%;
    background: var(--column-strip);
    border-left: 1px solid var(--column-edge);
    border-right: 1px solid var(--column-edge);
  }
  .artist-list {
    position: absolute;
    left: 87px;
    top: 88px;
    list-style: none;
    font-weight: 700;
    font-size: 27px;
    line-height: 35px;
    color: var(--ink);
  }
</style>
</head>
<body>
  <article class="postcard">
    <h1 class="postcard__title">Twelve Painters</h1>
    <div class="postcard__artwork" role="img" aria-label="Photograph of two paintbrushes resting on a colourful abstract painting"></div>
    <aside class="artist-column">
      <div class="artist-column__strip"></div>
      <ul class="artist-list">
        <li>Ashford</li>
        <li>Brennick</li>
        <li>Carrow</li>
        <li>Dalby</li>
        <li>Elwin</li>
        <li>Farrelly</li>
        <li>Gaskin</li>
        <li>Holm</li>
        <li>Ivers</li>
        <li>Jessup</li>
        <li>Kettner</li>
        <li>Lorne</li>
        <li>Pell</li>
        <li>Sorley</li>
      </ul>
    </aside>
  </article>
</body>
</html>
```